Larkfield Rowhomes - Billboard design for our newly renovated townhome community

We have a 5' wide x 4' tall billboard at the entrance to our apartment community, that needs to have the acrylic insert replaced. It is a 2 sided sign, and we are planning to use the same image on both sides. We are called Larkfield Rowhomes, and have 48 townhomes that are all 2 bedroom, 1 1/2 bath. A few things we would like to get across on the signage: "Newly Renovated" "2 bed 1 1/2 bath" "Full size W/D in every home" " New Appliances" I've included our parent company's logo - this is the only image I could think of, but it might not be worth having it on the sign. We are in Colorado, so mountain theme could be nice and also sunshine/sun since we are called "Larkfield"

Industry/Entity Type

Apartment

Font styles to use
Sans Serif

Requirements
Must have
• Newly Renovated
2 bed 1 1/2 bath
Full size W/D in every home
Virtual Tours available
www.brambletonhomesco.example
855 - 413 - 9286
Nice to have
• We are located in Colorado - possibly mountain theme? Since our community is called "Larkfield Rowhomes" - anything bright with Sun / Sunshine might look really nice as well.

```html
<!DOCTYPE html>
<html lang="en">
<head>
<meta charset="UTF-8">
<title>Larkfield Rowhomes – Billboard</title>
<link rel="stylesheet" href="https://fonts.googleapis.com/css2?family=Oswald:wght@500;600;700&family=Montserrat:wght@700&display=swap">
<style>
  :root {
    --navy: #16223f;
    --ink: #0d0d0d;
    --white: #ffffff;
    --bullet: #f7e9a0;
    --red: #c70a0a;
    --red-deep: #8e0000;
    --silver-1: #ffffff;
    --silver-2: #d9d9d9;
    --brown: #5a3d0e;
    --page: #f4f4f4;
  }
  * { margin: 0; padding: 0; box-sizing: border-box; }
  html, body { width: 1200px; height: 1101px; overflow: hidden; background: var(--page); }
  body { display: flex; align-items: center; justify-content: center; }

  .billboard {
    position: relative;
    width: 1200px;
    height: 950px;
    overflow: hidden;
    font-family: "Oswald", "Arial Narrow", sans-serif;
  }

  .scenery {
    position: absolute; inset: 0;
    background:
      radial-gradient(ellipse 220px 150px at 590px 370px, rgba(255,255,255,0.75), rgba(255,255,255,0) 70%),
      linear-gradient(180deg,
        #ece6ec 0%, #f1dccb 18%, #f6d2a0 30%, #f2c57c 37%,
        #6f7fa6 44%, #56699a 52%, #3e4f78 62%,
        #2a3a3a 72%, #1c2620 82%, #121713 100%);
  }

  .headline {
    position: absolute; left: 48px; top: 30px;
    color: var(--navy);
    font-weight: 700;
    text-transform: uppercase;
    line-height: 0.92;
    letter-spacing: -2px;
  }
  .headline .line-1 { display: block; font-size: 158px; }
  .headline .line-2 { display: block; font-size: 158px; }

  .parent-brand {
    position: absolute; left: 770px; top: 130px; width: 390px;
    text-align: center;
    color: var(--navy);
    font-weight: 500;
    font-size: 34px;
  }

  .features {
    position: absolute; left: 60px; top: 540px;
    list-style: none;
    color: var(--white);
    font-weight: 500;
    font-size: 58px;
    line-height: 74px;
    letter-spacing: -0.5px;
  }
  .features li { display: flex; align-items: center; }
  .features li::before {
    content: ""; width: 20px; height: 20px; border-radius: 50%;
    background: var(--bullet); margin-right: 36px;
  }

  .footer-wave { position: absolute; inset: 0; width: 1200px; height: 950px; }

  .contact {
    position: absolute; left: 24px; top: 790px;
    display: flex; align-items: center; gap: 18px;
  }
  .contact .phone-icon { width: 118px; height: 130px; flex: none; }
  .contact .phone-number {
    display: block;
    color: var(--ink);
    font-weight: 600;
    font-size: 100px;
    line-height: 96px;
    letter-spacing: -1px;
    white-space: nowrap;
  }
  .contact .website {
    display: block;
    font-family: "Montserrat", "Arial", sans-serif;
    font-weight: 700;
    font-size: 35px;
    color: var(--ink);
    margin-top: 2px;
    white-space: nowrap;
  }

  .tour-badge {
    position: absolute; left: 815px; top: 587px;
    width: 318px; height: 318px; border-radius: 50%;
    background: radial-gradient(circle at 40% 30%, var(--silver-1), var(--silver-2) 70%, #b9b9b9);
    box-shadow: 0 14px 18px -10px rgba(0,0,0,0.35);
  }
  .tour-badge .core {
    position: absolute; inset: 17px; border-radius: 50%; overflow: hidden;
    background: radial-gradient(circle at 45% 35%, #f21b1b, var(--red) 55%, var(--red-deep));
    color: var(--white); text-align: center; text-transform: uppercase;
  }
  .tour-badge .big {
    display: block; font-weight: 700; font-size: 70px; line-height: 62px;
    letter-spacing: -1px;
  }
  .tour-badge .big:first-child { margin-top: 60px; }
  .tour-badge .band {
    position: absolute; left: 0; right: 0; top: 190px; height: 54px;
    background: #141414;
    font-weight: 600; font-size: 44px; line-height: 54px;
  }
</style>
</head>
<body>
  <main class="billboard">
    <div class="scenery" role="img" aria-label="Photo of snow-capped Colorado mountains under a sunset sky with pine forest in the foreground"></div>

    <h1 class="headline"><span class="line-1">Newly</span><span class="line-2">Renovated</span></h1>

    <p class="parent-brand">Crestline Communities</p>

    <ul class="features">
      <li>2 Bed 1 1/2 Bath</li>
      <li>Full Size W/D in Every Home</li>
    </ul>

    <svg class="footer-wave" viewBox="0 0 1200 950" aria-hidden="true">
      <defs>
        <linearGradient id="silver" x1="0" y1="0" x2="1" y2="0">
          <stop offset="0" stop-color="#e2e2e2"/>
          <stop offset="0.5" stop-color="#ffffff"/>
          <stop offset="1" stop-color="#dcdcdc"/>
        </linearGradient>
      </defs>
      <path d="M0,678 C140,770 330,790 560,760 C760,735 880,690 1010,680 L1200,740 L1200,950 L0,950 Z" fill="url(#silver)"/>
      <path class="red-swoosh" d="M0,678 C140,770 330,790 560,760 C760,735 880,690 1010,680" fill="none" stroke="var(--red)" stroke-width="7"/>
      <path class="red-swoosh" d="M1090,680 L1200,720 L1200,755 L1090,705 Z" fill="var(--red)"/>
    </svg>

    <div class="contact">
      <svg class="phone-icon" viewBox="0 0 118 130" aria-hidden="true">
        <rect x="40" y="4" width="70" height="122" rx="10" fill="none" stroke="var(--brown)" stroke-width="9"/>
        <line x1="62" y1="14" x2="88" y2="14" stroke="var(--brown)" stroke-width="4"/>
        <circle cx="75" cy="116" r="4" fill="var(--brown)"/>
        <path d="M70,30 L24,62 C8,72 4,86 6,102 L8,118 L46,118 L46,78 L70,58 Z" fill="var(--brown)"/>
        <rect x="94" y="44" width="22" height="14" rx="7" fill="var(--brown)"/>
        <rect x="94" y="62" width="22" height="14" rx="7" fill="var(--brown)"/>
        <rect x="94" y="80" width="22" height="14" rx="7" fill="var(--brown)"/>
        <rect x="94" y="98" width="20" height="14" rx="7" fill="var(--brown)"/>
      </svg>
      <div class="contact-text">
        <span class="phone-number">855 - 413 - 9286</span>
        <span class="website">www.brambletonhomesco.example</span>
      </div>
    </div>

    <div class="tour-badge">
      <div class="core">
        <span class="big">Virtual</span>
        <span class="big">Tours</span>
        <span class="band">Available</span>
      </div>
    </div>
  </main>
</body>
</html>
```